Speisekarten-Design für italienisches Restaurant im Golfclub mit Blick auf die Alpen
Zielgruppe
Italienisches Restaurant im Golfclub mit Blick auf die Alpen (bei gutem Wetter)
Aufgabenstellung
Karte muss weiterhin bearbeitet werden könne. Es geht um ein Design das optisch anspricht aber nicht übertrieben ist. Die Blätter kommen später in eine Menukarte die noch in Auftrag gegeben werden.
Im Idealfall kann der Designer hierfür auch was mit designen das an einen Firma weitergeben werden kann um die 'Umschläge zu erstellen. Logo kann muss nicht mit drin sein. Es geht auch sehr um die einfache Darstellung des Ganzen.

```html
<!DOCTYPE html>
<html lang="de">
<head>
<meta charset="utf-8">
<title>Ristorante Valmonte – Monatskarte</title>
<link rel="stylesheet" href="https://fonts.googleapis.com/css2?family=Oswald:wght@500;600&family=Arimo:ital,wght@0,400;1,400&display=swap">
<style>
  :root {
    --header-bg: #231f20;
    --paper: #f0dab8;
    --paper-light: #f7e9d2;
    --ink: #3d3b3b;
    --gold: #c9a24a;
  }
  * { margin: 0; padding: 0; box-sizing: border-box; }
  html, body { width: 735px; height: 1200px; overflow: hidden; }
  body { background: var(--paper); font-family: "Arimo", Arial, sans-serif; color: var(--ink); }
  .menu { position: relative; width: 735px; height: 1200px; overflow: hidden; background: var(--paper); }
  .masthead {
    height: 180px; background: var(--header-bg);
    display: flex; flex-direction: column; align-items: center; justify-content: center;
    color: var(--gold); font-family: "Oswald", sans-serif; font-weight: 500; text-align: center;
  }
  .masthead .brand-name { font-size: 40px; letter-spacing: 2px; line-height: 1; }
  .masthead .brand-sub { font-size: 10px; letter-spacing: 4px; margin-top: 10px; text-transform: uppercase; }
  .deco { position: absolute; }
  .deco-leaves {
    left: 350px; top: 188px; width: 400px; height: 435px;
    background: radial-gradient(ellipse at 60% 45%, var(--paper-light) 0%, rgba(247,233,210,0.6) 45%, rgba(240,218,184,0) 72%);
  }
  .deco-vegetables {
    left: -20px; top: 770px; width: 290px; height: 440px;
    background: radial-gradient(ellipse at 35% 60%, var(--paper-light) 0%, rgba(247,233,210,0.6) 45%, rgba(240,218,184,0) 72%);
  }
  .menu-title {
    position: absolute; left: 101px; top: 226px;
    font-family: "Oswald", sans-serif; font-weight: 600; font-size: 48px; line-height: 54px;
    text-transform: uppercase; color: var(--ink); letter-spacing: -0.5px;
  }
  .dish { position: absolute; left: 104px; width: 560px; font-size: 12.6px; line-height: 16px; }
  .dish .it { display: block; }
  .dish .de { display: block; font-style: italic; margin-top: 7px; }
  .dish .de.upright { font-style: normal; }
  .price {
    position: absolute; right: 82px;
    font-family: "Oswald", sans-serif; font-weight: 500; font-size: 26px; line-height: 1;
    color: var(--ink); letter-spacing: -0.5px;
  }
  .price sup { font-size: 13px; vertical-align: top; position: relative; top: -1px; margin-left: 1px; }
</style>
</head>
<body>
<main class="menu">
  <header class="masthead">
    <div class="brand-name">RISTORANTE VALMONTE</div>
    <div class="brand-sub">im Golfclub Hohe Weide</div>
  </header>

  <div class="deco deco-leaves" role="img" aria-label="Weiße Strichzeichnung von Gemüse und Blättern"></div>
  <div class="deco deco-vegetables" role="img" aria-label="Weiße Strichzeichnung von Karotte und Knoblauch"></div>

  <h1 class="menu-title">Carta del mese /<br>Monatskarte</h1>

  <section class="dish" style="top:381px">
    <span class="it">Insalata Valeriana<br>gamberetti / uova / funghi/ salmone affumicato</span>
    <span class="de">Feldsalat mit Crevetten / Eier<br>Rote Zwiebeln/ Räucherlachs/ Champignons (gebraten)</span>
  </section>
  <div class="price" style="top:391px">9<sup>00</sup></div>

  <section class="dish" style="top:478px">
    <span class="it">Prosciutto di parma/ rucola / ciliegino / burrata</span>
    <span class="de">Parmaschinken mit Rucola / Cherrytomaten/ Burrata</span>
  </section>
  <div class="price" style="top:487px">9<sup>00</sup></div>

  <section class="dish" style="top:555px">
    <span class="it">Trofie al pesto di rucola con mandorle e pinoli</span>
    <span class="de">Pasta mit Rucola Pesto / Mandeln / Pinienkerne</span>
  </section>
  <div class="price" style="top:566px">12<sup>00</sup></div>

  <section class="dish" style="top:633px">
    <span class="it">Tortelloni ripieni con gamberetti / salmone /<br>mascarpone / salsa rosa al limoni</span>
    <span class="de upright">Tortelloni (hausgemacht) gefüllt mit Crevetten<br>Lachs/ Mascarpone/ Zitrone-Rosasoße</span>
  </section>
  <div class="price" style="top:645px">14<sup>00</sup></div>

  <section class="dish" style="top:729px">
    <span class="it">Gnocchi fatti in casa con ragù e mozzarella di bufala</span>
    <span class="de">Kartoffeln Gnocchi (hausgemacht) Büffel Mozzarella<br>Hackfleischsoße (Kalb-Rind)/ Ofen überbacken</span>
  </section>
  <div class="price" style="top:740px">12<sup>00</sup></div>

  <section class="dish" style="top:809px">
    <span class="it">Risotto primavera</span>
    <span class="de">Risotto mit Gemüse/ Zucchini/ Karotten/ Bohnen/ Broccoli</span>
  </section>
  <div class="price" style="top:820px">12<sup>00</sup></div>

  <section class="dish" style="top:886px">
    <span class="it">Saltimbocca di vitello alla romana</span>
    <span class="de">Kalbsschnitzel im Parmaschinken Mantel/ Salbei/ Weissweinsoße</span>
  </section>
  <div class="price" style="top:898px">18<sup>00</sup></div>

  <section class="dish" style="top:966px">
    <span class="it">Gamberoni al limone</span>
    <span class="de">Garnelen in Zitronensosse</span>
  </section>
  <div class="price" style="top:977px">21<sup>00</sup></div>

  <section class="dish" style="top:1045px">
    <span class="it">Fegato alla veneziana</span>
    <span class="de">Kalbsleber nach Benezianischer Art/ Salbei/ Weisswein</span>
  </section>
  <div class="price" style="top:1056px">17<sup>00</sup></div>
</main>
</body>
</html>
```